Family Ranch with a hobby vineyard needs 2 wine labels for our first harvest

Design 2 wine labels (front and back) with the Brindor Ranch logo.
Label 1:
Sauvignon Blanc
Alc. 12.5% by Vol.
Palos Verdes Peninsula - add as the region
Year 2022
Label 2:
Cabernet Sauvignon
Alc. 13.5% by Vol.
Year 2022
For the back label design:
GOVERNMENT WARNING: (1) According to the Surgeon General, women
should not drink alcoholic beverages during pregnancy because of the risk of
birth defects. (2) Consumption of alcoholic beverages impairs your ability to
drive a car or operate machinery, and may cause health problems.
Contains Sulfates.
750ML
I just received the bottles and have attached a picture.
Look and feel
Each slider illustrates characteristics of the customer's brand and the style your logo design should communicate.

```html
<!DOCTYPE html>
<html lang="en">
<head>
<meta charset="utf-8">
<title>Brindor Ranch – Wine Labels 2022</title>
<link rel="stylesheet" href="https://fonts.googleapis.com/css2?family=Cinzel:wght@400;600&family=Cormorant+Garamond:wght@400&display=swap">
<style>
  :root {
    --backdrop: #231f1f;
    --label-black: #121111;
    --cab-red: #b5100a;
    --cab-red-deep: #7d0804;
    --blanc-gold: #e3b21a;
    --blanc-gold-deep: #b88507;
    --foil-gold: #d8b57c;
    --foil-gold-light: #f4e2bd;
    --text-light: #f3efe8;
    --strip-text: #231b10;
  }
  html, body {
    margin: 0;
    width: 1200px;
    height: 1200px;
    overflow: hidden;
    background: var(--backdrop);
  }
  .label-set {
    position: absolute;
    inset: 0;
    display: flex;
    justify-content: center;
    align-items: center;
    gap: 60px;
  }
  .wine-label {
    position: relative;
    width: 450px;
    height: 700px;
    background: var(--label-black);
    overflow: hidden;
  }
  .brand-band {
    position: absolute;
    left: 0; top: 0;
    width: 100%;
    height: 195px;
    display: flex;
    flex-direction: column;
    align-items: center;
    justify-content: center;
    gap: 14px;
  }
  .wine-label--cabernet .brand-band {
    background: linear-gradient(90deg, var(--cab-red-deep), var(--cab-red) 35%, var(--cab-red) 65%, var(--cab-red-deep));
  }
  .wine-label--blanc .brand-band {
    background: linear-gradient(90deg, var(--blanc-gold-deep), var(--blanc-gold) 35%, var(--blanc-gold) 65%, var(--blanc-gold-deep));
  }
  .brand-mark {
    width: 44px; height: 44px;
    border-radius: 50%;
    background: var(--text-light);
  }
  .brand-name {
    font-family: "Cinzel", serif;
    font-weight: 600;
    font-size: 44px;
    letter-spacing: 2px;
    color: var(--text-light);
    margin: 0;
  }
  .horse-art {
    position: absolute;
    left: 0; top: 210px;
    width: 300px;
    height: 440px;
    background: radial-gradient(ellipse at 45% 30%, #9c9c9c 0%, #5a5a5a 30%, #262626 60%, var(--label-black) 80%);
  }
  .wine-details {
    position: absolute;
    right: 32px;
    top: 400px;
    text-align: right;
    color: var(--text-light);
  }
  .varietal {
    font-family: "Cinzel", serif;
    font-weight: 600;
    font-size: 34px;
    line-height: 1.1;
    margin: 0;
  }
  .vintage {
    font-family: "Cormorant Garamond", serif;
    font-size: 46px;
    color: var(--foil-gold-light);
    margin: 80px 0 0;
  }
  .abv {
    font-family: "Cormorant Garamond", serif;
    font-size: 16px;
    color: var(--foil-gold);
    margin: 18px -20px 0 0;
  }
  .region-map {
    position: absolute;
    left: 200px; top: 640px;
    width: 46px; height: 26px;
    background: radial-gradient(ellipse, #333 0%, var(--label-black) 75%);
  }
  .region-strip {
    position: absolute;
    left: 0; bottom: 0;
    width: 100%;
    height: 34px;
    background: linear-gradient(90deg, #8a6a3c, var(--foil-gold-light) 20%, var(--foil-gold) 50%, var(--foil-gold-light) 80%, #8a6a3c);
    display: flex;
    align-items: center;
    justify-content: center;
    font-family: "Cinzel", serif;
    font-weight: 600;
    font-size: 16px;
    letter-spacing: 1.5px;
    color: var(--strip-text);
  }
</style>
</head>
<body>
  <main class="label-set">
    <section class="wine-label wine-label--cabernet">
      <header class="brand-band">
        <span class="brand-mark"></span>
        <p class="brand-name">Brindor Ranch</p>
      </header>
      <div class="horse-art" role="img" aria-label="Monochrome illustration of a horse head with flowing mane"></div>
      <div class="wine-details">
        <h2 class="varietal">Cabernet<br>Sauvignon</h2>
        <p class="vintage">2022</p>
        <p class="abv">ALC. 13.5% BY VOL.</p>
      </div>
      <div class="region-map" role="img" aria-label="Small outline map of the Palos Verdes Peninsula"></div>
      <div class="region-strip">Palos Verdes Peninsula</div>
    </section>

    <section class="wine-label wine-label--blanc">
      <header class="brand-band">
        <span class="brand-mark"></span>
        <p class="brand-name">Brindor Ranch</p>
      </header>
      <div class="horse-art" role="img" aria-label="Monochrome illustration of a horse head with flowing mane"></div>
      <div class="wine-details">
        <h2 class="varietal">Sauvignon<br>Blanc</h2>
        <p class="vintage">2022</p>
        <p class="abv">ALC. 12.5% BY VOL.</p>
      </div>
      <div class="region-map" role="img" aria-label="Small outline map of the Palos Verdes Peninsula"></div>
      <div class="region-strip">Palos Verdes Peninsula</div>
    </section>
  </main>
</body>
</html>
```